Cause bitches need love too!

I am creating an ad campaign. It will be a series of featured dogs in our shelter and they will contain a picture of the dog wich should be big enough to see on a yard sign and will change every week. I am placing the signs so that they lead you to the shelter. This is why I am also including the copy that says "you're almost there".

I have 4 tag lines:

1. Find unconditional Love.
2. She'll Love you furever!
3. He'll always listen.
4. Meet your new BFF

You're almost there 318 W Harrowgate Ln
Open 10 - 7/Tues-Sat

The dimensions for the sign are 24" wide and 18" high

Every week we will have a different picture of a different dog (hopefully last week's dog gets adopted). Anyhow, I am printing out yard signs, meaning that instead of printing 160 different signs it would be ideal just to replace the photo. So far the copy that is permanent is: "You're almost there. 318 W. Harrowgate Ln."

I could silhouette the image of the dog as well and super impose it on the sign, that's also a consideration, but ideally if I could have 4 tag lines I could print 40 signs of each and just replace the photo manually each week from my printer that would save costs.
Updates

Not enough designs to chose from and I edited the brief and committed to pay no matter what to increase the amount of designs as per your suggestions.

Target Market(s)

Animal lovers

Industry/Entity Type

Campaign

Font styles to use
Sans Serif

Colors

Designer to choose colors to be used in the design.

Requirements
Must have
• The dimensions for the sign are 24" wide and 18" high
Nice to have
• I want the signs to be hip, they should have a positive feel to them. You can alter the photos if you like. I am even open to new copy if you think something else works better.

```html
<!DOCTYPE html>
<html lang="en">
<head>
<meta charset="utf-8">
<title>Shelter Yard Sign Series</title>
<link href="https://fonts.googleapis.com/css2?family=Rubik:wght@500;700;800&display=swap" rel="stylesheet">
<style>
  :root {
    --page: #ffffff;
    --pink: #ed1557;
    --peach: #f9c77f;
    --purple: #a35fa8;
    --sky: #52b3db;
    --white: #ffffff;
    --yellow: #fff22d;
    --band: rgba(70, 66, 62, 0.5);
    --tan-dog-a: #b9874e;
    --tan-dog-b: #3a2e24;
    --grey-dog-a: #9c9088;
    --grey-dog-b: #e9e4de;
  }
  * { margin: 0; padding: 0; box-sizing: border-box; }
  html, body {
    width: 1200px; height: 1200px; overflow: hidden;
    background: var(--page);
    font-family: "Rubik", Arial, sans-serif;
  }
  .sign-grid {
    position: absolute; left: 0; top: 137px;
    width: 1200px; height: 882px;
    display: grid;
    grid-template-columns: 600px 600px;
    grid-template-rows: 441px 441px;
  }
  .sign { position: relative; overflow: hidden; color: var(--white); }
  .sign--pink { background: var(--pink); }
  .sign--peach { background: var(--peach); }
  .sign--purple { background: var(--purple); }
  .sign--sky { background: var(--sky); }

  .dog-photo { position: absolute; top: 122px; width: 272px; height: 319px; }
  .dog-photo--right { left: 328px; }
  .dog-photo--left { left: 0; top: 74px; width: 352px; height: 367px; }
  .dog-photo--tan { background: radial-gradient(ellipse at 45% 35%, var(--tan-dog-a) 0%, #8a6235 45%, var(--tan-dog-b) 100%); border-radius: 46% 40% 0 0 / 30% 30% 0 0; }
  .dog-photo--grey { background: radial-gradient(ellipse at 40% 40%, var(--grey-dog-b) 0%, var(--grey-dog-a) 55%, #6f655f 100%); border-radius: 40% 46% 0 0 / 26% 30% 0 0; }

  .tagline { position: absolute; font-weight: 700; line-height: 1; letter-spacing: -0.5px; text-transform: uppercase; white-space: nowrap; }

  .directions { position: absolute; top: 280px; font-weight: 700; font-size: 27px; line-height: 37px; text-transform: uppercase; letter-spacing: -0.4px; white-space: nowrap; }
  .directions--left { left: 22px; }
  .directions--right { right: 28px; text-align: right; }

  .hours-band { position: absolute; left: 0; right: 0; top: 370px; height: 54px; background: var(--band); }
  .hours { position: absolute; top: 50%; transform: translateY(-50%); color: var(--yellow); font-weight: 700; font-size: 37px; letter-spacing: -0.8px; white-space: nowrap; }
  .hours--left { left: 22px; }
  .hours--right { right: 22px; }
</style>
</head>
<body>
  <main class="sign-grid">
    <section class="sign sign--pink">
      <div class="dog-photo dog-photo--right dog-photo--tan" role="img" aria-label="Photo of the featured shelter dog, a tan and black mixed breed"></div>
      <h2 class="tagline" style="left:24px;top:32px;font-size:56px;">Find</h2>
      <h2 class="tagline" style="left:24px;top:86px;font-size:56px;">Unconditional</h2>
      <h2 class="tagline" style="left:24px;top:138px;font-size:82px;">Love.</h2>
      <p class="directions directions--left">You're almost there<br>318 W Harrowgate Ln</p>
      <div class="hours-band"><p class="hours hours--left">OPEN 10 - 7/TUES-SAT</p></div>
    </section>

    <section class="sign sign--peach">
      <div class="dog-photo dog-photo--right dog-photo--tan" role="img" aria-label="Photo of the featured shelter dog, a tan and black mixed breed"></div>
      <h2 class="tagline" style="left:28px;top:38px;font-size:52px;">She'll love you</h2>
      <h2 class="tagline" style="left:28px;top:90px;font-size:76px;">Furever!</h2>
      <p class="directions directions--left">You're almost there<br>318 W Harrowgate Ln</p>
      <div class="hours-band"><p class="hours hours--left">OPEN 10 - 7/TUES-SAT</p></div>
    </section>

    <section class="sign sign--purple">
      <div class="dog-photo dog-photo--left dog-photo--grey" role="img" aria-label="Photo of the featured shelter dog, a grey and white pit bull mix"></div>
      <h2 class="tagline" style="left:72px;top:26px;font-size:48px;word-spacing:12px;">He'll always</h2>
      <h2 class="tagline" style="right:22px;top:80px;font-size:92px;">Listen</h2>
      <p class="directions directions--right">You're almost there<br>318 W Harrowgate Ln</p>
      <div class="hours-band"><p class="hours hours--right">OPEN 10 - 7/TUES-SAT</p></div>
    </section>

    <section class="sign sign--sky">
      <div class="dog-photo dog-photo--left dog-photo--grey" role="img" aria-label="Photo of the featured shelter dog, a grey and white pit bull mix"></div>
      <h2 class="tagline" style="left:36px;top:28px;font-size:66px;">Meet your new</h2>
      <h2 class="tagline" style="right:44px;top:100px;font-size:100px;">BFF</h2>
      <p class="directions directions--right">You're almost there<br>318 W Harrowgate Ln</p>
      <div class="hours-band"><p class="hours hours--right">OPEN 10 - 7/TUES-SAT</p></div>
    </section>
  </main>
</body>
</html>
```